Luxury Wine Label for New Startup Winery

We need a wine label for our new winery startup. We have worked with a local designer but do not feel the resulting label / logo have the elevation required to present our brand as a luxury wine. Our winery is called "Harrowgate Vineyards" and we are focused on extremely high quality hand crafted artisan and estate wines from the Pacific Northwest.
We would like to see designs that utilize a tree line, or other imagery that represents the "Harrowgate" part of our company name. Another interesting feature could be wood grain.
A logo will be required based on your design so please design with this in mind:
This logo should be consistent with the wine bottle label design, and should be representative of our high end exclusive wine while giving a sense of place (Oregon/ Pacific Northwest.)
I will supply an image of the design we received from our local designer, PLEASE NOTE: in general we do like wood grain and tree line concepts but feel the execution was poorly done.
ATTN: Logo design should be suitable for use on: Bottles (Red wine/rose/white wine), Bussiness cards, vehicle signage, business signage, etc
P.S.:
If you have a design that is not outside the box we are still interested in seeing it.
Label is for a burgundy style bottle with a label height of 3.5 - 4" and a width of 3.5-4"
any label <= 4"x4" and >=3.5"x3.5" will be acceptable:
HOWEVER Width should be greater than or equal to height due to the bottle format
Target Market(s)
Wine enthusiasts with adequate discretionary budgets to afford $100 bottles of wine.
Industry/Entity Type
Wine / Winery
Requirements
Must have
- A sense of luxury, a feel of exclusivity, and a theme consistent with our product and brand name
Nice to have
- Tree line, wood grain or other wood themes. Serif fonts
Should not have
- anything cheesy, off topic, hard to read script fonts or anything that makes the label hard to read from a few feet away or too busy

```html
<!DOCTYPE html>
<html lang="en">
<head>
<meta charset="utf-8">
<title>Harrowgate Vineyards – Wine Label</title>
<link rel="stylesheet" href="https://fonts.googleapis.com/css2?family=Cinzel:wght@400;600;700&display=swap">
<style>
  :root {
    --paper: #ffffff;
    --bronze-light: #8c6840;
    --bronze-mid: #74532c;
    --bronze-dark: #5f3c14;
    --wine-deep: #4a0507;
    --wine-mid: #5e0a0c;
    --wine-bright: #6e0c0e;
    --title-gold: #8a7640;
  }
  * { margin: 0; padding: 0; box-sizing: border-box; }
  html, body {
    width: 1200px;
    height: 1200px;
    overflow: hidden;
    background: var(--paper);
  }
  .canvas {
    position: relative;
    width: 1200px;
    height: 1200px;
    display: flex;
    align-items: center;
    justify-content: center;
  }
  .label {
    position: relative;
    width: 720px;
    height: 720px;
    padding: 24px;
    background: linear-gradient(90deg,
      var(--bronze-light) 0%, var(--bronze-dark) 13%, var(--bronze-mid) 28%,
      var(--bronze-light) 40%, var(--bronze-dark) 55%, var(--bronze-dark) 64%,
      var(--bronze-light) 80%, var(--bronze-dark) 100%);
  }
  .label-field {
    position: relative;
    width: 100%;
    height: 100%;
    background: linear-gradient(100deg,
      var(--wine-deep) 0%, var(--wine-deep) 35%, var(--wine-mid) 48%,
      var(--wine-bright) 65%, var(--wine-bright) 100%);
  }
  .winery-name {
    position: absolute;
    top: 40px;
    left: 0;
    width: 100%;
    text-align: center;
    font-family: "Cinzel", serif;
    font-weight: 400;
    font-size: 56px;
    line-height: 72px;
    letter-spacing: 1px;
    color: var(--title-gold);
    padding-left: 12px;
  }
  .emblem-panel {
    position: absolute;
    left: 141px;
    top: 197px;
    width: 390px;
    height: 294px;
    background: linear-gradient(90deg,
      var(--bronze-light) 0%, var(--bronze-dark) 18%, var(--bronze-mid) 33%,
      var(--bronze-light) 48%, var(--bronze-dark) 63%, var(--bronze-light) 78%,
      var(--bronze-dark) 100%);
  }
  .emblem-art {
    position: absolute;
    left: 86px;
    top: 24px;
    width: 217px;
    height: 234px;
    border-radius: 50% 50% 20% 20% / 55% 55% 15% 15%;
    background: radial-gradient(ellipse at 50% 40%, rgba(94,20,10,0.55) 0%, rgba(94,20,10,0.25) 55%, rgba(94,20,10,0) 75%);
  }
  .wine-type {
    position: absolute;
    left: 0;
    width: 100%;
    top: 518px;
    text-align: center;
    font-family: "Cinzel", serif;
    font-weight: 700;
    font-size: 150px;
    line-height: 150px;
    letter-spacing: 2px;
    background: linear-gradient(90deg,
      var(--bronze-dark) 0%, var(--bronze-dark) 20%, var(--bronze-light) 30%,
      var(--bronze-dark) 42%, var(--bronze-mid) 60%, var(--bronze-dark) 72%,
      var(--bronze-light) 85%, var(--bronze-dark) 100%);
    -webkit-background-clip: text;
    background-clip: text;
    color: transparent;
  }
</style>
</head>
<body>
  <main class="canvas">
    <section class="label" aria-label="Harrowgate Vineyards wine label">
      <div class="label-field">
        <h1 class="winery-name">Harrowgate<br>Vineyards</h1>
        <div class="emblem-panel">
          <div class="emblem-art" role="img" aria-label="Line illustration of a leafy tree"></div>
        </div>
        <p class="wine-type">WINE</p>
      </div>
    </section>
  </main>
</body>
</html>
```